8x8 Social Media Ad - Harbor Summit Expo

Attention Real Estate Agents
Please join us for our
Quarterly Real Estate Training Expo
The 2nd Saturday of February, May, August and November
Our Next Training Expo is _________________________________
From 9 am to 1 pm
at
Marlowe Suites Fernridge Station
4187 Copperleaf Lane, Greenbelt, MD 20770
Scheduled Speakers
9:00 am - Desmond Pryce - Orientation
9:30 am - Terrell Oakes - Multiple Income Streams / Keystone Track
10:00 am - Lorna Beckett - Marketing though Social Media
10:45 am - Raul Denning - Generating Business through Kelp-Nest
11:30 am - Tunde Adesemi - Real Estate Investing
12:15 pm - Marcus Oyelowo - (Main Speaker) Training Topic TBA
For more information call Desmond Pryce at (240) 555-0192 or email dpryce@harborsummithomes.example

```html
<!DOCTYPE html>
<html lang="en">
<head>
<meta charset="utf-8">
<title>Harbor Summit Expo – Quarterly Real Estate Training Expo</title>
<link href="https://fonts.googleapis.com/css2?family=Montserrat:wght@500;600;700;800&display=swap" rel="stylesheet">
<style>
  :root {
    --teal: #0f8a8c;
    --teal-dark: #0b6f74;
    --teal-deep: #0a4f66;
    --navy: #123a5c;
    --ink: #111111;
    --paper: #ffffff;
    --panel: #e9e9e9;
    --light: #f2f2f2;
  }
  * { box-sizing: border-box; margin: 0; padding: 0; }
  html, body { width: 1200px; height: 1200px; overflow: hidden; background: var(--paper); }
  body { font-family: "Montserrat", sans-serif; color: var(--ink); position: relative; }

  .hero {
    position: absolute; left: 0; top: 0; width: 1200px; height: 640px;
    background: linear-gradient(115deg, #0d3f63 0%, #125a73 35%, #148a80 55%, #0f8a8c 75%, #2a8c9e 100%);
  }
  .hero-edge { position: absolute; left: 0; top: 600px; width: 1200px; height: 60px; }
  .lower {
    position: absolute; left: 0; top: 640px; width: 1200px; height: 560px;
    background: linear-gradient(180deg, #ececec 0%, #ffffff 40%);
  }

  .invite-pill {
    position: absolute; left: 371px; top: 62px; width: 486px; height: 57px;
    border: 2px solid #fff; border-radius: 30px;
    color: #fff; font-weight: 700; font-size: 29px; letter-spacing: 0.5px;
    display: flex; align-items: center; justify-content: center;
  }
  .title {
    position: absolute; left: 0; top: 145px; width: 1200px; text-align: center;
    color: #fff; font-weight: 800; font-size: 66px; line-height: 80px;
    text-shadow: 2px 3px 4px rgba(0,0,0,0.35);
  }

  .speaker {
    position: absolute; top: 324px; width: 162px; height: 242px;
    background: var(--paper); border-radius: 81px;
    box-shadow: 0 0 0 7px rgba(255,255,255,0.25);
    text-align: center;
  }
  .speaker .photo {
    width: 127px; height: 127px; border-radius: 50%;
    margin: 14px auto 0;
    background: radial-gradient(circle at 50% 40%, #8a9aa4 0%, #56656e 60%, #3b4750 100%);
  }
  .speaker .name { margin-top: 22px; font-weight: 700; font-size: 17px; line-height: 24px; }

  .info-panel {
    position: absolute; left: 52px; top: 718px; width: 315px; height: 293px;
    background: var(--panel); border-radius: 8px 0 0 8px; text-align: center;
  }
  .info-panel .when { margin-top: 20px; font-weight: 700; font-size: 18.5px; line-height: 26px; }
  .accent { color: var(--teal); }
  .info-panel .next { margin-top: 14px; font-weight: 600; font-size: 15px; }
  .hours {
    display: inline-block; margin-top: 6px; padding: 4px 18px;
    background: var(--teal); color: #fff; font-weight: 700; font-size: 18px; border-radius: 16px;
  }
  .pin-rule { margin: 10px auto 0; width: 170px; height: 18px; display: block; }
  .venue { margin-top: 4px; font-weight: 500; font-size: 13.8px; line-height: 20px; }

  .side-label {
    position: absolute; left: 367px; top: 718px; width: 45px; height: 293px; background: var(--ink);
    display: flex; align-items: center; justify-content: center;
  }
  .side-label span {
    writing-mode: vertical-rl; color: #fff; font-weight: 800; font-size: 18px;
  }

  .schedule {
    position: absolute; left: 412px; top: 718px; width: 736px; height: 293px;
    border-collapse: collapse; border-radius: 0 8px 8px 0; overflow: hidden;
  }
  .schedule td { height: 48.8px; font-size: 16.5px; font-weight: 600; border-bottom: 1px solid rgba(255,255,255,0.6); white-space: nowrap; }
  .schedule tr:last-child td { border-bottom: none; }
  .schedule .time { width: 129px; padding-left: 28px; background: var(--teal-dark); color: #fff; }
  .schedule .who { width: 188px; padding-left: 27px; background: var(--light); font-weight: 700; border-bottom-color: #d5d5d5; }
  .schedule .topic { padding-left: 31px; color: #fff; background: linear-gradient(90deg, var(--teal-deep), var(--teal)); }

  .brand {
    position: absolute; left: 52px; top: 1096px; width: 262px;
    display: flex; align-items: center; gap: 8px; white-space: nowrap;
    font-weight: 700; font-size: 15px; color: var(--teal-dark);
  }
  .brand .mark { width: 16px; height: 16px; background: var(--teal-dark); flex: none; }
  .divider { position: absolute; top: 1070px; width: 1px; height: 80px; background: #999; }

  .call-lead { position: absolute; left: 351px; top: 1068px; width: 471px; text-align: center; font-weight: 500; font-size: 18px; }
  .call-pill {
    position: absolute; left: 351px; top: 1101px; width: 471px; height: 41px; border-radius: 21px;
    background: linear-gradient(90deg, var(--ink) 0 58%, var(--teal-dark) 58% 100%);
    display: flex; align-items: center; justify-content: center; gap: 10px;
    color: #fff; font-weight: 700; font-size: 21px;
  }
  .call-pill svg { width: 24px; height: 24px; }

  .contact {
    position: absolute; left: 852px; display: flex; align-items: center; gap: 6px;
    font-weight: 500; font-size: 14px; white-space: nowrap;
  }
  .contact svg { width: 21px; height: 21px; flex: none; }
</style>
</head>
<body>

<section class="hero" role="img" aria-label="Photo of a modern glass high-rise against a teal sky"></section>
<svg class="hero-edge" viewBox="0 0 1200 60" preserveAspectRatio="none" aria-hidden="true">
  <path d="M0 30 C60 18 110 40 170 26 S290 14 350 30 S470 44 540 22 S660 10 730 30 S860 42 930 26 S1060 14 1120 30 S1180 24 1200 20 L1200 60 L0 60 Z" fill="#ececec"/>
</svg>
<section class="lower"></section>

<div class="invite-pill">PLEASE JOIN US FOR OUR</div>
<h1 class="title">QUARTERLY REAL ESTATE<br>TRAINING EXPO</h1>

<div class="speaker" style="left:58px"><div class="photo" role="img" aria-label="Portrait of Desmond Pryce"></div><p class="name">Desmond<br>Pryce</p></div>
<div class="speaker" style="left:242px"><div class="photo" role="img" aria-label="Portrait of Terrell Oakes"></div><p class="name">Terrell<br>Oakes</p></div>
<div class="speaker" style="left:427px"><div class="photo" role="img" aria-label="Portrait of Lorna Beckett"></div><p class="name">Lorna<br>Beckett</p></div>
<div class="speaker" style="left:610px"><div class="photo" role="img" aria-label="Portrait of Raul Denning"></div><p class="name">Raul<br>Denning</p></div>
<div class="speaker" style="left:795px"><div class="photo" role="img" aria-label="Portrait of Tunde Adesemi"></div><p class="name">Tunde<br>Adesemi</p></div>
<div class="speaker" style="left:980px"><div class="photo" role="img" aria-label="Portrait of Marcus Oyelowo"></div><p class="name">Marcus<br>Oyelowo</p></div>

<aside class="info-panel">
  <p class="when">The <span class="accent">2nd Saturday</span> of<br><span class="accent">February, May, August</span><br>and <span class="accent">November</span></p>
  <p class="next">Our Next Training Expo is</p>
  <span class="hours">From 9 am to 1 pm</span>
  <svg class="pin-rule" viewBox="0 0 170 18" aria-hidden="true">
    <line x1="0" y1="9" x2="70" y2="9" stroke="#0f8a8c" stroke-width="1.5"/>
    <line x1="100" y1="9" x2="170" y2="9" stroke="#0f8a8c" stroke-width="1.5"/>
    <circle cx="85" cy="9" r="7" fill="none" stroke="#0f8a8c" stroke-width="1.3"/>
    <path d="M85 13 C82 10 81 8 81 6.5 A4 4 0 0 1 89 6.5 C89 8 88 10 85 13 Z" fill="#0f8a8c"/>
  </svg>
  <p class="venue">at Marlowe Suites<br>Fernridge Station 4187<br>Copperleaf Lane, Greenbelt,<br>MD 20770</p>
</aside>

<div class="side-label"><span>Scheduled Speakers</span></div>

<table class="schedule">
  <tr><td class="time">9:00 am</td><td class="who">Desmond Pryce</td><td class="topic">Orientation</td></tr>
  <tr><td class="time">9:30 am</td><td class="who">Terrell Oakes</td><td class="topic">Multiple Income Streams / Keystone Track</td></tr>
  <tr><td class="time">10:00 am</td><td class="who">Lorna Beckett</td><td class="topic">Marketing though Social Media</td></tr>
  <tr><td class="time">10:45 am</td><td class="who">Raul Denning</td><td class="topic">Generating Business through Kelp-Nest</td></tr>
  <tr><td class="time">11:30 am</td><td class="who">Tunde Adesemi</td><td class="topic">Real Estate Investing</td></tr>
  <tr><td class="time">12:15 pm</td><td class="who">Marcus Oyelowo</td><td class="topic">(Main Speaker) Training Topic TBA</td></tr>
</table>

<div class="brand"><span class="mark"></span><span>Harbor Summit Realty Group</span></div>
<div class="divider" style="left:327px"></div>
<div class="divider" style="left:838px"></div>

<p class="call-lead">For more information call</p>
<div class="call-pill">
  <span>Desmond Pryce at</span>
  <svg viewBox="0 0 24 24" aria-hidden="true"><circle cx="12" cy="12" r="11" fill="#fff"/><path d="M8 6 L10 6 L11 9 L9.5 10.3 C10.3 12 11.8 13.5 13.7 14.5 L15 13 L18 14 L18 16 C18 17 17 18 16 18 C10.5 17.6 6.4 13.5 6 8 C6 7 7 6 8 6 Z" fill="#0b6f74"/></svg>
  <span>(240) 555-0192</span>
</div>

<div class="contact" style="top:1080px">
  <svg viewBox="0 0 22 22" aria-hidden="true"><circle cx="11" cy="11" r="10" fill="none" stroke="#0b6f74" stroke-width="1.3"/><rect x="6" y="7.5" width="10" height="7" fill="none" stroke="#333" stroke-width="1.1"/><path d="M6 7.5 L11 11.5 L16 7.5" fill="none" stroke="#333" stroke-width="1.1"/></svg>
  <span>dpryce@<span class="accent">harborsummithomes</span>.example</span>
</div>
<div class="contact" style="top:1113px">
  <svg viewBox="0 0 22 22" aria-hidden="true"><circle cx="11" cy="11" r="10" fill="none" stroke="#0b6f74" stroke-width="1.3"/><circle cx="11" cy="11" r="5.5" fill="none" stroke="#333" stroke-width="1.1"/><ellipse cx="11" cy="11" rx="2.5" ry="5.5" fill="none" stroke="#333" stroke-width="1"/><line x1="5.5" y1="11" x2="16.5" y2="11" stroke="#333" stroke-width="1"/></svg>
  <span>www.<span class="accent">harborsummithomes</span>.example</span>
</div>

</body>
</html>
```